Website Design for Car Donations

Revise current site www.ridesforhonor.org

Sites i like:

https://www.wheelsformilitary.org

https://autogivingforheroes.org

https://plinkmock.com/144490c6/screen/39053423

Coding

Coded - Design and coding required

Number of Pages Required

1 page

```html
<!DOCTYPE html>
<html lang="en">
<head>
<meta charset="utf-8">
<title>Rides For Honor – Donate Your Vehicle</title>
<link href="https://fonts.googleapis.com/css2?family=Raleway:wght@500;600;700;800&family=Open+Sans:wght@400;600;700&display=swap" rel="stylesheet">
<style>
:root{
  --navy:#0c2a6b;
  --navy-deep:#0a2260;
  --red:#d40d12;
  --ink:#333a48;
  --muted:#555c6a;
  --panel:#f3f3f3;
  --line:#d6d9df;
  --white:#fff;
}
*{box-sizing:border-box;margin:0;padding:0}
html,body{width:1200px;height:3025px;overflow:hidden}
body{font-family:"Open Sans",Arial,sans-serif;color:var(--ink);background:var(--white);position:relative}
h1,h2,h3,h4,.nav,.brand{font-family:"Raleway",Arial,sans-serif}
.section{position:absolute;left:0;width:1200px}

/* header */
.site-header{top:0;height:95px;background:var(--navy)}
.brand{position:absolute;left:160px;top:28px;display:flex;align-items:center;gap:10px;color:var(--white);font-weight:800;font-size:28px;letter-spacing:.5px}
.brand-dot{width:30px;height:30px;border-radius:50%;background:var(--red)}
.nav{position:absolute;left:525px;top:36px;display:flex;gap:22px;color:var(--white);font-weight:600;font-size:15px}
.header-phone{position:absolute;right:160px;top:12px;color:var(--white);font:700 22px "Open Sans",sans-serif}
.btn-donate-small{position:absolute;right:160px;top:47px;width:112px;height:33px;background:var(--red);color:var(--white);font:600 15px "Open Sans",sans-serif;display:flex;align-items:center;justify-content:center;border-radius:3px}

/* hero */
.hero{top:95px;height:505px;background:var(--panel)}
.hero-photo{position:absolute;left:0;top:0;width:650px;height:505px;background:linear-gradient(135deg,#c9b7a4 0%,#9a8b72 45%,#d8d0c6 100%)}
.carousel-dots{position:absolute;left:525px;top:462px;display:flex;gap:5px}
.carousel-dots span{width:10px;height:10px;border-radius:50%;background:#fff;opacity:.7}
.carousel-dots span:first-child{background:transparent;border:2px solid #fff;opacity:1}
.donate-form{position:absolute;left:690px;top:42px;width:348px}
.donate-form h1{color:var(--navy);font-size:23px;font-weight:700;line-height:1.3}
.donate-form p{font-size:12.5px;font-weight:600;color:#222;margin:12px 0 18px 2px}
.field-row{display:flex;gap:6px;margin-bottom:8px}
.field{flex:1;height:35px;background:var(--white);border:1px solid #ccc;border-radius:2px;font-size:11px;color:#888;padding:10px 12px;position:relative}
.field.select::after{content:"";position:absolute;right:10px;top:15px;border:4px solid transparent;border-top-color:#555}
.btn-submit{margin-top:8px;height:42px;background:var(--red);color:var(--white);font:700 14px "Open Sans",sans-serif;display:flex;align-items:center;justify-content:center;gap:6px;border-radius:3px}

/* how to donate */
.how{top:600px;height:398px;background:var(--white)}
.section-title{text-align:center;color:var(--navy);font-weight:700}
.how .section-title{font-size:28px;margin-top:32px}
.steps{position:absolute;left:0;top:90px;width:1200px}
.step{position:absolute;width:260px;text-align:center}
.step-icon{width:164px;height:164px;margin:0 auto;border-radius:50%;border:3px solid var(--red);padding:6px}
.step-icon div{width:100%;height:100%;border-radius:50%;background:var(--navy);display:flex;align-items:center;justify-content:center}
.step h3{color:var(--red);font-size:19px;font-weight:600;margin:14px 0 10px}
.step p{font-size:11.5px;line-height:1.65;color:var(--ink)}

/* why donate */
.why{top:998px;height:460px;background:#efefef}
.why-photo{position:absolute;right:0;top:0;width:600px;height:460px;background:linear-gradient(90deg,#efefef 0%,#cbb89c 30%,#8c7757 60%,#d9d2c4 100%)}
.why h2{position:absolute;left:160px;top:48px;color:var(--navy);font-size:32px;font-weight:700}
.why-list{position:absolute;left:160px;top:120px;width:470px;list-style:none}
.why-list li{position:relative;padding-left:22px;font-size:11.5px;line-height:1.6;margin-bottom:18px;color:var(--ink)}
.why-list li::before{content:"";position:absolute;left:2px;top:5px;width:9px;height:9px;background:var(--red);transform:rotate(45deg)}

/* impact band */
.impact{top:1458px;height:464px;background:linear-gradient(180deg,#0e2f78,#0a2260)}
.impact h2{color:var(--white);font-size:31px;text-align:center;margin-top:40px;line-height:1.25;font-weight:700}
.impact-cards{position:absolute;left:160px;top:148px;display:flex;gap:27px}
.impact-card{width:276px;text-align:center}
.impact-card .photo{height:214px;border:6px solid var(--white)}
.impact-card h4{color:var(--white);font-size:17px;font-weight:600;margin-top:14px}

/* faq */
.faq{top:1922px;height:478px;background:var(--white)}
.faq .section-title{font-size:31px;margin-top:50px}
.faq-col{position:absolute;top:112px;width:428px}
.faq-col.left{left:160px}.faq-col.right{left:608px}
.faq-item{height:50px;border:1px solid var(--line);border-radius:25px;margin-bottom:10px;display:flex;align-items:center;justify-content:space-between;padding:0 22px;font-size:13px;font-weight:600;color:#222;box-shadow:0 1px 3px rgba(0,0,0,.06)}
.faq-item .sign{color:var(--red);font-size:20px;font-weight:700}
.faq-item.open{background:var(--red);color:var(--white);border-color:var(--red);position:relative}
.faq-item.open .sign{color:var(--white)}
.faq-item.open::after{content:"";position:absolute;left:40px;bottom:-10px;border:10px solid transparent;border-bottom:0;border-top-color:var(--red)}
.faq-answer{border:1px solid var(--line);border-radius:14px;padding:18px 28px;font-size:11.5px;line-height:1.7;color:var(--ink);margin-top:-2px}

/* program */
.program{top:2400px;height:333px;background:var(--panel)}
.program .section-title{font-size:27px;margin-top:38px}
.features{position:absolute;top:110px;left:0;width:1200px}
.feature{position:absolute;width:220px;text-align:center}
.feature .icon{height:62px;display:flex;align-items:center;justify-content:center}
.feature h4{color:var(--red);font-size:13px;font-weight:600;line-height:1.4;margin:14px 0 14px}
.feature p{font-size:11px;line-height:1.7;color:var(--muted)}

/* footer */
.site-footer{top:2733px;height:292px;background:var(--navy-deep);color:var(--white)}
.site-footer .brand{top:44px;font-size:22px}
.site-footer .brand-dot{width:24px;height:24px}
.call-label{position:absolute;left:160px;top:118px;font-size:16px}
.footer-phone{position:absolute;left:160px;top:144px;font:700 29px "Open Sans",sans-serif}
.call-note{position:absolute;left:160px;top:190px;font-size:11px}
.footer-col{position:absolute;top:44px}
.footer-col h4{font-size:16px;font-weight:700;letter-spacing:.5px;margin-bottom:16px}
.footer-col p,.footer-col li{font-size:11.5px;line-height:1.7;list-style:none}
.badge{width:80px;height:34px;background:#e8e8e8;border-radius:4px;margin-bottom:12px}
.badge.round{width:54px;height:30px;border-radius:15px;background:#bcd0e8}
.footer-rule{position:absolute;left:160px;right:160px;top:222px;height:1px;background:rgba(255,255,255,.2)}
.socials{position:absolute;left:160px;top:240px;display:flex;gap:12px}
.socials span{width:36px;height:36px;border-radius:50%;border:1.5px solid rgba(255,255,255,.8)}
.copyright{position:absolute;right:160px;top:253px;font-size:11px}
</style>
</head>
<body>

<header class="section site-header">
  <div class="brand"><span class="brand-dot"></span>RIDES FOR HONOR</div>
  <nav class="nav"><span>How to donate</span><span>Why donate</span><span>FAQ</span><span>About</span></nav>
  <div class="header-phone">1-800-555-0142</div>
  <div class="btn-donate-small">Donate Now!</div>
</header>

<section class="section hero">
  <div class="hero-photo" role="img" aria-label="Photo of a military father, daughter and mother smiling on a sofa"></div>
  <div class="carousel-dots"><span></span><span></span><span></span></div>
  <form class="donate-form">
    <h1>Donate Your Vehicle and Give Back to Disabled Veterans</h1>
    <p>To donate your vehicle call or fill out the form below.</p>
    <div class="field-row"><div class="field">Name</div><div class="field">Last Name</div></div>
    <div class="field-row"><div class="field">Phone:</div></div>
    <div class="field-row"><div class="field">Email:</div></div>
    <div class="field-row"><div class="field">Address</div><div class="field">City</div></div>
    <div class="field-row"><div class="field select">State</div><div class="field">Zip Code</div></div>
    <div class="field-row"><div class="field select">Choose year</div><div class="field">Model</div></div>
    <div class="btn-submit">CLICK HERE TO DONATE NOW
      <svg width="14" height="14" viewBox="0 0 14 14"><circle cx="7" cy="7" r="7" fill="#fff"/><path d="M5.5 4l3 3-3 3" stroke="#d40d12" stroke-width="2" fill="none"/></svg>
    </div>
  </form>
</section>

<section class="section how">
  <h2 class="section-title">How to Donate</h2>
  <div class="steps">
    <div class="step" style="left:170px">
      <div class="step-icon"><div>
        <svg width="56" height="64" viewBox="0 0 56 64"><rect x="8" y="4" width="40" height="46" rx="2" fill="#fff"/><g stroke="#0c2a6b" stroke-width="3"><line x1="16" y1="16" x2="40" y2="16"/><line x1="16" y1="24" x2="40" y2="24"/><line x1="16" y1="32" x2="40" y2="32"/><line x1="16" y1="40" x2="32" y2="40"/></g><path d="M28 48v12M24 56l4 4 4-4" stroke="#fff" stroke-width="2.5" fill="none"/></svg>
      </div></div>
      <h3>1. Fill out the online form</h3>
      <p>Donating your vehicle is easy and<br>donation is accepted nationwide, or<br>Call us at 1-800-555-0142</p>
    </div>
    <div class="step" style="left:465px">
      <div class="step-icon"><div>
        <svg width="60" height="64" viewBox="0 0 60 64"><path d="M30 2v14a6 6 0 1 1-6 6" stroke="#fff" stroke-width="3" fill="none"/><path d="M12 44l6-10h24l6 10v12H12z" fill="#fff"/><circle cx="20" cy="50" r="3" fill="#0c2a6b"/><circle cx="40" cy="50" r="3" fill="#0c2a6b"/><rect x="14" y="56" width="8" height="6" fill="#fff"/><rect x="38" y="56" width="8" height="6" fill="#fff"/></svg>
      </div></div>
      <h3>2. We tow the vehicle</h3>
      <p>Any vehicles are accepted and we will<br>arrange to pick up your vehicle when it<br>is most convenient for you.</p>
    </div>
    <div class="step" style="left:760px">
      <div class="step-icon"><div>
        <svg width="56" height="64" viewBox="0 0 56 64"><rect x="14" y="2" width="28" height="18" fill="#fff"/><text x="22" y="16" font-size="12" font-family="Open Sans,sans-serif" fill="#0c2a6b" font-weight="700">$</text><rect x="6" y="22" width="44" height="38" fill="#fff"/><path d="M6 22l22 18 22-18M6 60l16-16M50 60L34 44" stroke="#0c2a6b" stroke-width="2.5" fill="none"/></svg>
      </div></div>
      <h3>3. Tax write-off</h3>
      <p>Once the vehicle donation is complete,<br>you will receive your tax deductible<br>vehicle donation receipt.</p>
    </div>
  </div>
</section>

<section class="section why">
  <div class="why-photo" role="img" aria-label="Photo of a young soldier in camouflage seated in a wheelchair"></div>
  <h2>Why donate your car to us</h2>
  <ul class="why-list">
    <li>IRS 501(c)3 Approved : Free 24/7 Pickup with No DMV Hassles.</li>
    <li>Free Local Towing : We will pick up your car donation, running or not, when it's most convenient, at home or work.</li>
    <li>Tax Deduction : We issue you an IRS tax receipt and get you the highest tax write-off possible.</li>
    <li>No Paperwork Hassles : We handle everything: DMV and IRS paperwork.</li>
    <li>Car donations help fund programs : And benefit Valor Path Foundation. An IRS 501(c)3 nonprofit organization.</li>
    <li>Schedule a Free Pickup : Complete the form and a representative will call you to arrange a convenient time to pickup your car.</li>
  </ul>
</section>

<section class="section impact">
  <h2>Donate your car to veterans<br>Make a difference</h2>
  <div class="impact-cards">
    <div class="impact-card"><div class="photo" role="img" aria-label="Photo of a saluting soldier beside rows of flags" style="background:linear-gradient(135deg,#6f8a4c,#b9423f 55%,#c9c3b0)"></div><h4>Active Duty</h4></div>
    <div class="impact-card"><div class="photo" role="img" aria-label="Photo of a veteran with a prosthetic leg seated on a step" style="background:linear-gradient(135deg,#c8b99f,#8d8a86 55%,#6f7b8c)"></div><h4>Wounded Heros</h4></div>
    <div class="impact-card"><div class="photo" role="img" aria-label="Photo of two older veterans in caps embracing" style="background:linear-gradient(135deg,#a9b7c9,#5d5246 50%,#c2a58a)"></div><h4>Support Veterans</h4></div>
  </div>
</section>

<section class="section faq">
  <h2 class="section-title">Frequently asked questions</h2>
  <div class="faq-col left">
    <div class="faq-item">What types of vehicles can be donated?<span class="sign">+</span></div>
    <div class="faq-item">What paperwork do I need to donate my vehicle?<span class="sign">+</span></div>
    <div class="faq-item open">Is my donated vehicle tax-deductible?<span class="sign">−</span></div>
    <div class="faq-answer">Yes, we are a 501(c)3 organization and have been approved by the IRS to receive donated items and issue a tax-deductible donation receipt for the item. Therefore, your vehicle donation may be 100% tax deductible based upon your personal tax situation.</div>
  </div>
  <div class="faq-col right">
    <div class="faq-item">What if the vehicle is not registered in my name?<span class="sign">+</span></div>
    <div class="faq-item">How much will I receive as a tax deduction for ..?<span class="sign">+</span></div>
    <div class="faq-item">Proin sit amet dui id leo eleifend blandit?<span class="sign">+</span></div>
    <div class="faq-item">When will I receive my tax receipt?<span class="sign">+</span></div>
    <div class="faq-item">How do I schedule a pick up?<span class="sign">+</span></div>
  </div>
</section>

<section class="section program">
  <h2 class="section-title">Car Donation Program</h2>
  <div class="features">
    <div class="feature" style="left:143px">
      <div class="icon"><div role="img" aria-label="Map of the United States" style="width:70px;height:44px;background:#0c2a6b;border-radius:10px 14px 8px 18px"></div></div>
      <h4>Donations<br>Accepted Nationwide</h4>
      <p>Sed ut perspiciatis unde omnis<br>sit voluptatem accusantium dolorue<br>laudantiutem accusantmota.</p>
    </div>
    <div class="feature" style="left:375px">
      <div class="icon"><svg width="62" height="52" viewBox="0 0 62 52"><path d="M4 26l8-18h38l8 18v16H4z" fill="#0c2a6b"/><rect x="18" y="12" width="26" height="12" fill="#fff"/><circle cx="14" cy="33" r="4" fill="#fff"/><circle cx="48" cy="33" r="4" fill="#fff"/><rect x="6" y="42" width="10" height="8" fill="#0c2a6b"/><rect x="46" y="42" width="10" height="8" fill="#0c2a6b"/></svg></div>
      <h4>All Vehicle<br>Types Welcome</h4>
      <p>Sed ut perspiciatis unde omnis<br>sit voluptatem accusantium dolorue<br>laudantiutem accusantmota.</p>
    </div>
    <div class="feature" style="left:605px">
      <div class="icon"><svg width="46" height="56" viewBox="0 0 46 56"><rect x="2" y="2" width="42" height="52" rx="3" fill="#0c2a6b"/><circle cx="14" cy="16" r="6" fill="#fff"/><g stroke="#fff" stroke-width="3"><line x1="24" y1="13" x2="38" y2="13"/><line x1="24" y1="20" x2="38" y2="20"/><line x1="9" y1="30" x2="38" y2="30"/><line x1="9" y1="38" x2="38" y2="38"/><line x1="9" y1="46" x2="30" y2="46"/></g></svg></div>
      <h4>Tax Deductible</h4>
      <p>Sed ut perspiciatis unde omnis<br>sit voluptatem accusantium dolorue<br>laudantiutem accusantmota.</p>
    </div>
    <div class="feature" style="left:835px">
      <div class="icon"><svg width="72" height="56" viewBox="0 0 72 56"><path d="M14 6l22 20" stroke="#0c2a6b" stroke-width="4"/><path d="M10 6v10a4 4 0 0 0 6 0" stroke="#0c2a6b" stroke-width="3" fill="none"/><path d="M6 30h34V18h14l10 12v14H6z" fill="#0c2a6b"/><rect x="44" y="21" width="9" height="8" fill="#fff"/><circle cx="18" cy="46" r="6" fill="#0c2a6b" stroke="#fff" stroke-width="2"/><circle cx="54" cy="46" r="6" fill="#0c2a6b" stroke="#fff" stroke-width="2"/></svg></div>
      <h4>Towing is Free</h4>
      <p>Sed ut perspiciatis unde omnis<br>sit voluptatem accusantium dolorue<br>laudantiutem accusantmota.</p>
    </div>
  </div>
</section>

<footer class="section site-footer">
  <div class="brand"><span class="brand-dot"></span>RIDES FOR HONOR</div>
  <div class="call-label">Call today to donate</div>
  <div class="footer-phone">1-800-555-0142</div>
  <div class="call-note">Live Operators Available - 7 Days A Week</div>
  <div class="footer-col" style="left:452px;width:220px">
    <h4>ABOUT</h4>
    <p>Car donations help fund programs and benefit Valor Path Foundation. An IRS 501(c)3 nonprofit organization. Schedule a Free Pickup: Complete the form and a representative will call you to arrange a convenient time to pickup your car.</p>
  </div>
  <div class="footer-col" style="left:738px">
    <h4>LINKS</h4>
    <ul><li>How to donate</li><li>Why donate</li><li>FAQ</li><li>About</li></ul>
  </div>
  <div class="footer-col" style="left:880px">
    <h4>SAFE &amp; SECURE</h4>
    <div class="badge" role="img" aria-label="Security badge"></div>
    <div class="badge round" role="img" aria-label="Certification badge"></div>
  </div>
  <div class="footer-rule"></div>
  <div class="socials">
    <span role="img" aria-label="Social link"></span><span role="img" aria-label="Social link"></span><span role="img" aria-label="Social link"></span><span role="img" aria-label="Social link"></span>
  </div>
  <div class="copyright">Copyrights © 2018 Rides for Honor. All rights reserved. Privacy Policy</div>
</footer>

</body>
</html>
```